Fernvale Craft Works business card design- Fine Art sculpture business (Contract guaranteed)

This business card is for a fine art business. Though we don't have a website up and running yet it should be up soon. I would like the business card to be elegant and fairly simple with a picture of one of my sculptures on the front (you might need to photoshop out the background) as well as my basic contact info (my name,phone # and e-mail). On the back I'd like it to be pretty simple with just "Notes" and some blank lines for writing in info.

Target Market(s)

High end artwork buyers

Industry/Entity Type

Art Gallery

Contact Information for Business Card

Marlo Prewitt Phone: (555) 213-4098 E-mail: marlo@quillbrookmail.com Facebook: @fernvalecraftworks Instagram: fernvalecraftworks

Colors

Designer to choose colors to be used in the design.

Requirements
Must have
• *A picture of one of my sculptures*, my name, business name (Fernvale Craft Works), e-mail, phone #, and a notes section on the back.
• Fernvale Craft Works
• Marlo Prewitt
• (555)213-4098
• marlo@quillbrookmail.com
• Facebook: @fernvalecraftworks
• Instagram: fernvalecraftworks
Nice to have
• It'd be nice if you can crop out the background in the sculpture pictures, which ever one you end up using.

```html
<!DOCTYPE html>
<html lang="en">
<head>
<meta charset="utf-8">
<title>Fernvale Craft Works – Business Cards</title>
<link href="https://fonts.googleapis.com/css2?family=Lato:wght@400;700&display=swap" rel="stylesheet">
<style>
  :root {
    --backdrop: #2a2a2b;
    --card: #ffffff;
    --card-shade: #f1f1f1;
    --ink: #2b2b2b;
    --brand-green: #1db36b;
    --rule: #a9a9a9;
    --stone-dark: #0f3d2e;
    --stone-mid: #1f7a5a;
    --stone-light: #5fcfa3;
    --base-dark: #141414;
  }
  * { box-sizing: border-box; margin: 0; padding: 0; }
  html, body {
    width: 1200px; height: 900px; overflow: hidden;
    background: var(--backdrop);
    font-family: "Lato", sans-serif;
  }
  .stage { position: relative; width: 1200px; height: 900px; }

  .card {
    position: absolute;
    width: 560px; height: 320px;
    background: linear-gradient(135deg, var(--card) 55%, var(--card-shade));
    overflow: hidden;
  }

  /* Back of card */
  .card--back { left: 360px; top: 100px; }
  .card--back .wordmark {
    position: absolute; left: 0; right: 0; top: 62px;
    text-align: center;
    font-size: 36px; font-weight: 400; color: var(--ink);
    letter-spacing: 1px;
  }
  .note-lines { position: absolute; left: 60px; right: 60px; top: 150px; }
  .note-line { height: 1px; background: var(--rule); margin-bottom: 38px; }
  .card--back .edge-band {
    position: absolute; left: 0; right: 0; bottom: 0; height: 12px;
    background: var(--brand-green);
  }

  /* Front of card */
  .card--front { left: 240px; top: 480px; }
  .sculpture {
    position: absolute; left: 40px; top: 18px; width: 150px; height: 286px;
    display: block;
  }
  .contact-block { position: absolute; left: 228px; top: 86px; right: 24px; }
  .card--front .wordmark {
    font-size: 32px; font-weight: 400; color: var(--ink);
    letter-spacing: 0.5px; margin-bottom: 18px;
  }
  .person-name {
    font-size: 24px; font-weight: 700; color: var(--brand-green);
    letter-spacing: 0.5px; margin-bottom: 14px;
  }
  .contact-line {
    display: flex; align-items: center; gap: 8px;
    font-size: 17px; color: var(--ink); margin-bottom: 6px;
  }
  .contact-line svg { width: 14px; height: 14px; flex: none; fill: var(--brand-green); }
</style>
</head>
<body>
<main class="stage">

  <section class="card card--back" aria-label="Card back">
    <p class="wordmark">Fernvale Craft Works</p>
    <div class="note-lines">
      <div class="note-line"></div>
      <div class="note-line"></div>
      <div class="note-line"></div>
    </div>
    <div class="edge-band"></div>
  </section>

  <section class="card card--front" aria-label="Card front">
    <svg class="sculpture" viewBox="0 0 150 286" role="img" aria-label="Photograph of a green malachite stone sculpture on a round black base">
      <defs>
        <linearGradient id="stoneTone" x1="0" y1="0" x2="1" y2="1">
          <stop offset="0" stop-color="var(--stone-light)"/>
          <stop offset="0.5" stop-color="var(--stone-mid)"/>
          <stop offset="1" stop-color="var(--stone-dark)"/>
        </linearGradient>
      </defs>
      <rect x="0" y="0" width="150" height="286" rx="8" fill="url(#stoneTone)"/>
      <rect x="0" y="236" width="150" height="50" rx="8" fill="var(--base-dark)"/>
    </svg>

    <div class="contact-block">
      <p class="wordmark">Fernvale Craft Works</p>
      <p class="person-name">MARLO PREWITT</p>
      <p class="contact-line">
        <svg viewBox="0 0 16 16" aria-hidden="true"><path d="M3.6 1.5l2.2 2.6-1.3 1.6c.8 1.9 2.2 3.3 4.1 4.2l1.6-1.3 2.6 2.2-1.4 2.4C6.3 12.8 3.2 9.7 1.3 4.6z"/></svg>
        (555) 213-4098
      </p>
      <p class="contact-line">
        <svg viewBox="0 0 16 16" aria-hidden="true"><path d="M1 3h14v10H1z M1.8 3.8L8 8.6l6.2-4.8" fill="var(--brand-green)"/><path d="M2 4l6 4.6L14 4" fill="none" stroke="#fff" stroke-width="1.2"/></svg>
        marlo.prewitt@quillbrookmail.com
      </p>
    </div>
  </section>

</main>
</body>
</html>
```